Email Marketing Campaign 50% discount and buy-2-get-1 offer

I would like to inform my customers of our special offers via a e-Newsletter/Marketing E-Mail.

The coding needs to be done by the designer.

I have most of the design and the message that we wish to convey our buyers.

The information is:

1. We have now 50% discount on all our carpets

2. We have a buy-2 get-1 free carpet offer

For both the above messages we have already banner style that we like to use in our Newsletter.
I have attached the banner and the designers can use it.

3. We have opened a new shop in Berlin Germany

Therefore we like to have a Sylish Newsletter design that fits our website and products using the banner idea and we wish to include the 3 messages.
Special note should be given that this newsletter is going to our previous buyers. Therefore they already know us, and we just like to inform them of our latest news and offer.

Target Market(s)

Upmarket buyers looking for a great deal

Industry/Entity Type

Marketing

Coding

Coded - Design and coding required

Number of Pages Required

1 page

Font styles to use
Sans Serif

Colors
e667a6
34a7d8

Requirements
Must have
• Clear explanation with excitement in the message
Nice to have
• To promote clearly the 3 for 2 with maybe an explanation and clear images describing what the promotion is and how it works.
• I.e. buy 2 get 1 extra carpet of your choice free
• Add carpets to checkout and the system will calculate automatically
• The lowest carpet in your selection of 3 is the free carpet

```html
<!DOCTYPE html>
<html lang="en">
<head>
<meta charset="utf-8">
<title>Heirloom Rugs Newsletter</title>
<link href="https://fonts.googleapis.com/css2?family=Lato:wght@300;400;700;900&display=swap" rel="stylesheet">
<style>
  :root {
    --pink: #d81b5f;
    --blue: #02aeef;
    --grey: #6f6f6f;
    --dark-grey: #555555;
    --white: #ffffff;
    --hero-dark: #3b3431;
    --hero-light: #b5a999;
  }
  * { margin: 0; padding: 0; box-sizing: border-box; }
  html, body { width: 800px; height: 1200px; overflow: hidden; background: var(--white); }
  body { font-family: 'Lato', sans-serif; }
  .newsletter { position: relative; width: 800px; height: 1200px; }

  .masthead { position: absolute; top: 0; left: 0; width: 800px; height: 120px; background: var(--white); }
  .brand { position: absolute; top: 36px; left: 0; width: 800px; text-align: center;
    font-size: 50px; font-weight: 300; color: var(--grey); letter-spacing: 1px; }
  .social { position: absolute; top: 78px; right: 32px; display: flex; gap: 14px; }
  .social span { width: 24px; height: 24px; border-radius: 50%; background: var(--dark-grey); }

  .hero { position: absolute; top: 120px; left: 0; width: 800px; height: 422px;
    background: linear-gradient(135deg, #8d8479 0%, var(--hero-light) 45%, #6b5a52 75%, var(--hero-dark) 100%); }
  .hero-photo { position: absolute; inset: 0; }
  .hero-shade { position: absolute; top: 0; left: 0; width: 213px; height: 422px; background: rgba(30, 26, 25, 0.55); }
  .hero-offer { position: absolute; inset: 0; color: var(--white); font-weight: 900; line-height: 1; }
  .hero-offer span { position: absolute; white-space: nowrap; }
  .offer-upto { left: 22px; top: 134px; font-size: 22px; }
  .offer-number { left: 14px; top: 150px; font-size: 90px; letter-spacing: -3px; }
  .offer-percent { left: 118px; top: 155px; font-size: 60px; }
  .offer-off { left: 123px; top: 209px; font-size: 24px; }
  .offer-sale { left: 16px; top: 223px; font-size: 86px; letter-spacing: -1px; }
  .offer-now { left: 100px; top: 305px; font-size: 21px; }
  .shop-now { position: absolute; left: 33px; top: 362px; width: 142px; height: 35px;
    background: var(--pink); color: var(--white); font-size: 16px; font-weight: 400; letter-spacing: 0.5px;
    display: flex; align-items: center; justify-content: center;
    clip-path: polygon(0 0, 100% 0, 94% 50%, 100% 100%, 0 100%, 6% 50%); text-decoration: none; }

  .bundle { position: absolute; top: 542px; left: 0; width: 800px; height: 258px; background: var(--white); }
  .bundle-title { position: absolute; left: 58px; top: 52px; font-size: 124px; font-weight: 900;
    color: var(--pink); line-height: 1; letter-spacing: 2px; }
  .bundle-text { position: absolute; left: 62px; top: 172px; width: 390px; font-size: 24px; font-weight: 700;
    color: var(--grey); line-height: 1.2; text-transform: uppercase; }
  .bundle-rugs { position: absolute; left: 458px; top: 26px; width: 342px; height: 232px;
    background: linear-gradient(90deg, #6d7171 0%, #6d7171 50%, #3b3fa0 52%, #4a43b2 78%, #e6a3a2 82%, #efb3b0 100%); }

  .extras { position: absolute; top: 800px; left: 0; width: 800px; height: 98px; background: var(--pink); }
  .extras-notch { position: absolute; left: 574px; top: -24px; }
  .extras-text { position: absolute; left: 107px; top: 37px; font-size: 23.5px; font-weight: 700; color: var(--white); white-space: nowrap; }
  .extras-box { position: absolute; left: 592px; top: 6px; width: 108px; height: 70px; background: #c9a477; border-radius: 3px; }

  .opening { position: absolute; top: 898px; left: 0; width: 800px; height: 302px; background: var(--blue); }
  .opening-title { position: absolute; left: 26px; top: 45px; width: 370px; font-size: 144px; font-weight: 700;
    color: var(--white); line-height: 122px; letter-spacing: -6px; white-space: nowrap; }
  .opening-photo { position: absolute; left: 400px; top: 44px; width: 358px; height: 155px;
    background: linear-gradient(180deg, #9fb8a0 0%, #e9e6e1 45%, #d8d4cf 70%, #b37c4e 100%); }
  .opening-text { position: absolute; left: 400px; top: 208px; width: 380px; font-size: 20px; font-weight: 700;
    color: var(--white); line-height: 1.2; text-transform: uppercase; }
</style>
</head>
<body>
<main class="newsletter">
  <header class="masthead">
    <div class="brand">Heirloom Rugs</div>
    <nav class="social" aria-label="Social links"><span></span><span></span><span></span></nav>
  </header>

  <section class="hero">
    <div class="hero-photo" role="img" aria-label="Living room with white sofa, coffee tables, marble fireplace and a faded vintage rug"></div>
    <div class="hero-shade"></div>
    <p class="hero-offer">
      <span class="offer-upto">up to</span>
      <span class="offer-number">50</span>
      <span class="offer-percent">%</span>
      <span class="offer-off">OFF</span>
      <span class="offer-sale">sale</span>
      <span class="offer-now">now on!</span>
    </p>
    <a class="shop-now" href="#">SHOP NOW</a>
  </section>

  <section class="bundle">
    <h2 class="bundle-title">B2GO</h2>
    <p class="bundle-text">Buy 2 get 1 extra carpet of your choice free</p>
    <div class="bundle-rugs" role="img" aria-label="Three overdyed vintage carpets in grey, blue and pink"></div>
  </section>

  <section class="extras">
    <svg class="extras-notch" width="60" height="26" viewBox="0 0 60 26"><polygon points="0,26 30,0 60,26" fill="var(--pink)"/></svg>
    <p class="extras-text">+ 40% EXTRA DISCOUNT + FREE SHIPPING</p>
    <div class="extras-box" role="img" aria-label="Open cardboard shipping box"></div>
  </section>

  <section class="opening">
    <h2 class="opening-title">NOW<br>OPEN</h2>
    <div class="opening-photo" role="img" aria-label="Bright modern showroom with white sofas, fireplace and dark rug"></div>
    <p class="opening-text">We have opened a new shop in Berlin Germany</p>
  </section>
</main>
</body>
</html>
```